Letter head for peronal trainer

Letter head top and bottom. Elite looking design that looks modern and prestigious for high end clients. Black, silver, reds etc. Attached are my business cards (2 x pdfs) and my website is: www.dariencrofte.example for style/ideas

Needs to look good when printing and be locked onto the page when people use my word docs on the computer, I don't want it to be 'clickable' if you know what I mean. Needs to work in A4 in portrait (and in landscape, for programme cards). I need it to be editable for when I adjust the text myself. Needs my contact details and social media details and title personal trainer (Central London/Greenwich/Blackheath) and Online Distance Coaching. . A little picture at the bottom too if it works (Like the vest one)

```html
<!DOCTYPE html>
<html lang="en">
<head>
<meta charset="utf-8">
<title>Darien Crofte – Letterhead</title>
<link rel="stylesheet" href="https://fonts.googleapis.com/css2?family=Exo+2:ital,wght@1,800&family=Open+Sans:wght@400;700&display=swap">
<style>
  :root {
    --paper: #ffffff;
    --backdrop: #e9e9e9;
    --ink: #222222;
    --ink-soft: #333333;
    --brand-red: #a51d22;
    --silver-light: #d9d9d9;
    --silver-mid: #a8a8a8;
    --silver-dark: #6f6f6f;
    --icon-grey: #8a8a8a;
  }
  * { margin: 0; padding: 0; box-sizing: border-box; }
  html, body {
    width: 893px; height: 1200px; overflow: hidden;
    background: var(--backdrop);
  }
  .letterhead {
    position: relative;
    width: 893px; height: 1200px;
    background: var(--paper);
    font-family: "Open Sans", Arial, sans-serif;
    color: var(--ink);
  }
  .brand-name {
    position: absolute; left: 34px; top: 36px;
    font-family: "Exo 2", Arial, sans-serif;
    font-weight: 800; font-style: italic;
    font-size: 52px; letter-spacing: 1px; line-height: 1;
    color: var(--silver-mid);
  }
  .brand-name span {
    background: linear-gradient(180deg, var(--silver-light) 0%, var(--silver-mid) 50%, var(--silver-dark) 100%);
    -webkit-background-clip: text; background-clip: text;
    color: transparent;
  }
  .brand-title {
    position: absolute; left: 38px; top: 97px;
    font-size: 17px; color: var(--ink);
  }
  .service-band {
    position: absolute; left: 16px; right: 0; top: 130px; height: 26px;
    background: var(--brand-red);
    clip-path: polygon(6px 0, 100% 0, 100% 100%, 0 100%);
  }
  .service-band p {
    padding-left: 16px;
    font-weight: 700; font-size: 16px; line-height: 26px;
    color: #ffffff; text-transform: uppercase;
  }
  .trainer-photo {
    position: absolute; right: 38px; top: 10px;
    width: 80px; height: 146px;
    background: linear-gradient(180deg, #9a9a9a 0%, #5a5a5a 55%, #3c3c3c 100%);
    border-radius: 30px 30px 4px 4px;
  }
  .contact-bar {
    position: absolute; left: 0; right: 0; top: 1154px;
    display: flex; justify-content: center; align-items: center; gap: 14px;
    font-size: 14px; color: var(--ink-soft);
  }
  .contact-item { display: flex; align-items: center; gap: 6px; white-space: nowrap; }
  .contact-item svg { width: 14px; height: 14px; fill: var(--icon-grey); }
</style>
</head>
<body>
<main class="letterhead">
  <header>
    <h1 class="brand-name"><span>DARIEN CROFTE</span></h1>
    <p class="brand-title">Personal Trainer (Central London/Greenwich/Blackheath)</p>
    <div class="service-band"><p>Online Distance Coaching</p></div>
    <div class="trainer-photo" role="img" aria-label="Black and white photo of the trainer standing shirtless in jeans"></div>
  </header>

  <footer class="contact-bar">
    <span class="contact-item">
      <svg viewBox="0 0 16 16" aria-hidden="true"><path d="M1 5c0-2 3-3 7-3s7 1 7 3v1h-4V5H5v1H1zM4 7h8l2 6H2z"/></svg>
      07700 900418
    </span>
    <span class="contact-item">
      <svg viewBox="0 0 16 16" aria-hidden="true"><path d="M1 6l7-4 7 4v8H1zm1.5 1v5.5h11V7L8 10z"/></svg>
      darien.pt@mail.example
    </span>
    <span class="contact-item">
      <svg viewBox="0 0 16 16" aria-hidden="true"><circle cx="8" cy="8" r="6"/></svg>
      @crofte_pt
    </span>
    <span class="contact-item">
      <svg viewBox="0 0 16 16" aria-hidden="true"><rect x="3" y="3" width="10" height="10"/></svg>
      DarienCrofteFitness
    </span>
    <span class="contact-item">
      <svg viewBox="0 0 16 16" aria-hidden="true"><circle cx="8" cy="8" r="6"/></svg>
      www.dariencrofte.example
    </span>
  </footer>
</main>
</body>
</html>
```